Simple, 1-Page Project - Life-saving AED Devices

We recently kicked off a project to bring all geographic location records for automatic emergency defibrillators (AEDs) in the State of New York online (instead of kept in paper in drawers). This hope is that is will ultimately save thousands of lives, as 9-1-1 operators will be able to quickly direct civilians to the nearest AED to bring to people suffering a cardiac event (e.g., a heart attack).

This page will be used to describe this effort, our progress thus far and how far we have left to go.

I am looking for a 1-page design - coded for both a responsive version for mobile devices and a traditional version - that would ***ideally*** plug into my existing WordPress site (https://brevalto-hub.org), but it's not a requirement.

Target Market(s)

General public (non-physicians/non-EMTs)

Requirements
Must have
• - Our logo (please note, our logo is the Harlow Ridge Chapter logo...attached)
Nice to have
• - Would be wonderful to have an area with a clickable map showing where the participating regions are - which, once clicked, will take to you their specific sites. Regions are large chunks of land encompassing multiple towns, NOT a singular, specific place A nice-looking Google Map, a la Quirbo Charts (https://quirbocharts.com/) would be cool if this were possible..
• - If you need a headline or page title, you can use: "Bringing AEDs in New York Online"
• - Would be nice if the design incorporated the color scheme of our brand (see attachment) and/or our main website: https://brevalto-hub.org/
• - Would be nice to have some AED imagery - I attached some common symbols seen in AED advertising for inspiration
Should not have
• - This is a serious topic, so the design should be respectful and not too silly/cartoonish
• - Stock images, if chosen, should be thoughtful and classy

```html
<!DOCTYPE html>
<html lang="en">
<head>
<meta charset="utf-8">
<title>Bringing AEDs in New York Online</title>
<link rel="stylesheet" href="https://fonts.googleapis.com/css2?family=EB+Garamond:wght@400;600;700&family=Open+Sans:wght@400;600&display=swap">
<style>
:root{
  --navy:#002d5a;
  --olive:#a8a27d;
  --white:#ffffff;
  --nav-text:#8a8f98;
  --rule:#e4e4e4;
  --alert:#d8343f;
  --alert-halo:rgba(216,52,63,.28);
  --panel-grey:#f1f1f1;
  --ink:#1f2328;
}
*{box-sizing:border-box;margin:0;padding:0}
html,body{width:1200px;height:1184px;overflow:hidden;background:var(--white);font-family:"Open Sans",sans-serif;color:var(--ink)}
.page{position:relative;width:1200px;height:1184px}

.site-header{position:absolute;left:0;top:0;width:1200px;height:79px;background:var(--white)}
.brand{position:absolute;left:73px;top:10px;display:flex;align-items:center}
.brand-mark{width:59px;height:59px;border-radius:50%;background:var(--navy)}
.brand-divider{width:1px;height:40px;background:var(--navy);margin:0 10px 0 12px}
.brand-name{font-family:"EB Garamond",serif;color:var(--navy);font-size:22px;line-height:1;font-weight:400}
.main-nav{position:absolute;left:589px;top:0;height:79px;display:flex}
.main-nav a{display:flex;align-items:center;justify-content:center;height:79px;border-left:1px solid var(--rule);font-family:"EB Garamond",serif;font-size:14.5px;color:var(--nav-text);text-decoration:none;white-space:nowrap}
.main-nav a.current{border-bottom:2px solid var(--navy)}
.main-nav .search{border-right:1px solid var(--rule)}

.title-bar{position:absolute;left:0;top:79px;width:1200px;height:50px;background:var(--navy);color:var(--white)}
.title-bar h2{position:absolute;left:114px;top:15px;font-family:"EB Garamond",serif;font-weight:400;font-size:15px}
.breadcrumb{position:absolute;right:114px;top:19px;font-family:"EB Garamond",serif;font-size:10px}

.hero{position:absolute;left:0;top:129px;width:1200px;height:171px;background:var(--olive);color:var(--white)}
.hero h1{position:absolute;left:0;width:1200px;top:34px;text-align:center;font-family:"EB Garamond",serif;font-weight:400;font-size:31px}
.hero p{position:absolute;left:116px;width:976px;top:82px;font-size:11.4px;line-height:16.8px}

.map-area{position:absolute;left:114px;top:358px;width:975px;height:507px;background:linear-gradient(135deg,#eceee6 0%,#e7ebde 40%,#e9e8e0 70%,#e3ebe3 100%)}
.map-markers{position:absolute;left:0;top:0}

.locator{position:absolute;left:127px;top:369px;width:240px;height:485px;background:var(--white);box-shadow:0 1px 4px rgba(0,0,0,.18)}
.locator-head{height:53px;background:var(--navy);color:var(--white);position:relative}
.locator-head svg{position:absolute;left:12px;top:14px}
.locator-head .loc{position:absolute;left:45px;top:12px;font-size:11.5px}
.locator-head .loc b{font-weight:600}
.locator-head .count{position:absolute;left:45px;top:29px;font-size:8.5px;opacity:.9}
.locator-search{height:34px;background:var(--panel-grey);position:relative}
.locator-search .field{position:absolute;left:13px;right:13px;top:7px;height:20px;border-bottom:1px solid #cfcfcf;font-size:11px;color:#a7a7a7;padding-top:2px}
.locator-search svg{position:absolute;right:16px;top:9px}
.nearby-label{position:absolute;left:13px;top:104px;font-size:8px;letter-spacing:1.3px;font-weight:600;color:#555}
.aed-list{list-style:none;position:absolute;left:13px;top:122px;width:214px}
.aed-list li{position:relative;height:60.5px;font-size:8.3px;line-height:11.5px;letter-spacing:.4px}
.aed-list .name{font-weight:600}
.aed-list svg{position:absolute;right:0;top:8px}

.site-footer{position:absolute;left:0;top:921px;width:1200px;height:263px;background:var(--navy);color:var(--white)}
.footer-col{position:absolute;top:50px;font-size:12px;line-height:16.5px}
.footer-col h3{font-family:"EB Garamond",serif;font-weight:700;font-size:12.5px;letter-spacing:.3px;margin-bottom:12px}
.footer-col ul{list-style:none}
.pages li{margin-bottom:13.5px}
.person{margin-bottom:14px}
.person strong{display:block;font-weight:600}
.contact p{margin-bottom:14px}
.contact strong{font-weight:600}
</style>
</head>
<body>
<div class="page">

<header class="site-header">
  <div class="brand">
    <div class="brand-mark"></div>
    <div class="brand-divider"></div>
    <div class="brand-name">Harlow Ridge Chapter</div>
  </div>
  <nav class="main-nav">
    <a class="current" style="width:79px">Home</a>
    <a style="width:109px">About HRACC</a>
    <a style="width:79px">Education</a>
    <a style="width:115px">Getting Involved</a>
    <a style="width:79px">Events</a>
    <a class="search" style="width:79px" aria-label="Search">
      <svg width="14" height="14" viewBox="0 0 14 14"><circle cx="5.6" cy="5.6" r="4.3" fill="none" stroke="#8a8f98" stroke-width="2"/><line x1="8.8" y1="8.8" x2="12.8" y2="12.8" stroke="#8a8f98" stroke-width="2.2" stroke-linecap="round"/></svg>
    </a>
  </nav>
</header>

<section class="title-bar">
  <h2>Bringing AEDs Online</h2>
  <div class="breadcrumb">You are here:&nbsp; Home / Bringing AEDs Online</div>
</section>

<section class="hero">
  <h1>Bringing AEDs in New York Online</h1>
  <p>Lorem ipsum dolor sit amet, consectetur adipiscing elit. Suspendisse feugiat posuere rutrum. Donec posuere sem vel nunc dictum pellentesque. Vivamus nisi diam, sagittis vel efficitur et, porttitor malesuada lorem. Quisque tincidunt tempus ante. Nam eu vulputate metus. Sed placerat augue in eros gravida, in maximus quam ornare. Integer ultrices fringilla ex id accumsan. Suspendisse ullamcorper, orci ut viverra vestibulum, enim nisi aliquet dolor, nec cursus massa orci nec ipsum.</p>
</section>

<section class="map-area" role="img" aria-label="Road map of the Albany and Mohawk Valley region of New York showing AED locations">
  <svg class="map-markers" width="975" height="507" viewBox="0 0 975 507">
    <defs>
      <g id="aed-marker">
        <circle r="35" fill="var(--alert-halo)"/>
        <circle r="22" fill="var(--alert)"/>
        <path d="M0 11 C-4 7 -12 2 -12 -4 C-12 -9 -6 -11 0 -6 C6 -11 12 -9 12 -4 C12 2 4 7 0 11Z" fill="#fff"/>
        <path d="M1.5 -7 L-3.5 0 L-0.5 0 L-2 5 L3.5 -2 L0.5 -2Z" fill="var(--alert)"/>
      </g>
    </defs>
    <use href="#aed-marker" x="432" y="79"/>
    <use href="#aed-marker" x="361" y="141"/>
    <use href="#aed-marker" x="528" y="220"/>
    <use href="#aed-marker" x="791" y="255"/>
    <use href="#aed-marker" x="888" y="360"/>
    <use href="#aed-marker" x="616" y="431"/>
  </svg>
</section>

<aside class="locator">
  <div class="locator-head">
    <svg width="20" height="26" viewBox="0 0 20 26"><path d="M10 0C4.5 0 0 4.4 0 9.8 0 17 10 26 10 26s10-9 10-16.2C20 4.4 15.5 0 10 0z" fill="#fff"/><circle cx="10" cy="9.5" r="3.6" fill="var(--navy)"/></svg>
    <div class="loc">Your Location: <b>10065</b></div>
    <div class="count">6 AEDs near 10065</div>
  </div>
  <div class="locator-search">
    <div class="field">Find an AED</div>
    <svg width="11" height="11" viewBox="0 0 14 14"><circle cx="5.6" cy="5.6" r="4.3" fill="none" stroke="#9a9a9a" stroke-width="1.8"/><line x1="8.8" y1="8.8" x2="12.8" y2="12.8" stroke="#9a9a9a" stroke-width="2" stroke-linecap="round"/></svg>
  </div>
  <div class="nearby-label">NEARBY</div>
  <ul class="aed-list">
    <li><div class="name">Ted Wind Bridge</div><div>721 N Hebron Rd, Little Falls, NY</div><div>7.3 miles away</div><svg width="14" height="14" viewBox="0 0 14 14"><circle cx="7" cy="7" r="6.3" fill="none" stroke="#555" stroke-width=".9"/><circle cx="7" cy="4" r=".8" fill="#555"/><rect x="6.4" y="5.8" width="1.2" height="4.6" fill="#555"/></svg></li>
    <li><div class="name">Lorem Ipsum</div><div>123 Main Rd, New York, NY</div><div>8.4 miles away</div><svg width="14" height="14" viewBox="0 0 14 14"><circle cx="7" cy="7" r="6.3" fill="none" stroke="#555" stroke-width=".9"/><circle cx="7" cy="4" r=".8" fill="#555"/><rect x="6.4" y="5.8" width="1.2" height="4.6" fill="#555"/></svg></li>
    <li><div class="name">Dignissim Suspendisse</div><div>456 Arbor St, Albany, NY</div><div>10.3 miles away</div><svg width="14" height="14" viewBox="0 0 14 14"><circle cx="7" cy="7" r="6.3" fill="none" stroke="#555" stroke-width=".9"/><circle cx="7" cy="4" r=".8" fill="#555"/><rect x="6.4" y="5.8" width="1.2" height="4.6" fill="#555"/></svg></li>
    <li><div class="name">Aenean Vel Elit</div><div>891 N Martin Rd, Syracuse, NY</div><div>12.9 miles away</div><svg width="14" height="14" viewBox="0 0 14 14"><circle cx="7" cy="7" r="6.3" fill="none" stroke="#555" stroke-width=".9"/><circle cx="7" cy="4" r=".8" fill="#555"/><rect x="6.4" y="5.8" width="1.2" height="4.6" fill="#555"/></svg></li>
    <li><div class="name">Volutpat Odio Facilisis</div><div>123 North St, New York, NY</div><div>14.3 miles away</div><svg width="14" height="14" viewBox="0 0 14 14"><circle cx="7" cy="7" r="6.3" fill="none" stroke="#555" stroke-width=".9"/><circle cx="7" cy="4" r=".8" fill="#555"/><rect x="6.4" y="5.8" width="1.2" height="4.6" fill="#555"/></svg></li>
    <li><div class="name">Risus Nec Feugiat</div><div>456 N Lantern Dr, Davenport, NY</div><div>20.1 miles away</div><svg width="14" height="14" viewBox="0 0 14 14"><circle cx="7" cy="7" r="6.3" fill="none" stroke="#555" stroke-width=".9"/><circle cx="7" cy="4" r=".8" fill="#555"/><rect x="6.4" y="5.8" width="1.2" height="4.6" fill="#555"/></svg></li>
  </ul>
</aside>

<footer class="site-footer">
  <div class="footer-col pages" style="left:114px">
    <h3>PAGES</h3>
    <ul><li>Home</li><li>About HRACC</li><li>Education</li><li>Events</li><li>Getting Invovled</li></ul>
  </div>
  <div class="footer-col governors" style="left:342px">
    <h3>GOVERNORS</h3>
    <div class="person"><strong>Elias Marrow, MD, FCCC</strong>Upstate Governor</div>
    <div class="person"><strong>Renata Vossberg, MD, FCCC</strong>Downstate Governor</div>
  </div>
  <div class="footer-col staff" style="left:622px">
    <h3>CHAPTER STAFF</h3>
    <div class="person"><strong>Liana Corvell, CAE</strong>Executive Director</div>
    <div class="person"><strong>Tomas Egerlund</strong>Program Associate</div>
  </div>
  <div class="footer-col contact" style="left:896px;width:220px">
    <h3>CONTACT</h3>
    <p><strong>The Harlow Ridge Chapter of the Cardiac Care Collegium</strong></p>
    <p>418 Quarry Lane, Suite 700<br>Harlow Ridge, HR 20417</p>
    <p>(555) 014-2290<br>hello@brevalto-hub.org</p>
  </div>
</footer>

</div>
</body>
</html>
```